K & R Fabrications HVAC Mechanical Contractor Business Card

We need a business card for a HVAC/Plumbing Mechanical Contractor. Our website is http://www.krfabrications-demo.com. We would like to include the picture of the person on the card. Pictures of people for mock-ups can be found on our website. The blue on our logo is our primary color. We'd like this to be bold yet professional without too many colors but with some color to make sure it stands out.

Industry/Entity Type

Business

Contact Information for Business Card

Font styles to use
Sans Serif

Colors
000000

Requirements
Must have
• Our logo
• Person's picture
• Company Name
• Company Phone
• Person's email address
• Person's phone number
Nice to have
• Company Address
Should not have
• Clip art

```html
<!DOCTYPE html>
<html lang="en">
<head>
<meta charset="utf-8">
<title>K &amp; R Fabrications – Business Card</title>
<link href="https://fonts.googleapis.com/css2?family=Lato:wght@400;700;900&display=swap" rel="stylesheet">
<style>
  :root {
    --brand-blue: #2456c4;
    --ink: #111111;
    --paper: #ffffff;
    --photo-dark: #2b2d30;
    --photo-light: #55595e;
    --backdrop: #e9e7e3;
    --card-edge: #0d0d0d;
  }
  * { box-sizing: border-box; margin: 0; padding: 0; }
  html, body {
    width: 1200px; height: 900px; overflow: hidden;
    background: var(--backdrop);
    font-family: "Lato", sans-serif;
  }
  .card {
    position: absolute; left: 100px; top: 164px;
    width: 1000px; height: 572px;
    background: var(--paper);
    border-bottom: 8px solid var(--card-edge);
    box-shadow: 0 18px 40px rgba(0,0,0,.25);
    overflow: hidden;
  }
  .card__band {
    position: absolute; left: 0; right: 0; bottom: 0; height: 142px;
    background: var(--brand-blue);
  }
  .card__band-raised {
    position: absolute; left: 480px; right: 0; top: 336px; bottom: 0;
    background: var(--brand-blue);
  }
  .card__photo {
    position: absolute; left: 0; top: 0; width: 540px; height: 422px;
  }
  .company {
    position: absolute; right: 40px; top: 32px; text-align: right;
    color: var(--ink);
  }
  .company__name {
    display: flex; align-items: center; justify-content: flex-end; gap: 14px;
    font-weight: 900; font-size: 30px; letter-spacing: .5px; text-transform: uppercase;
  }
  .company__mark { width: 32px; height: 32px; background: var(--brand-blue); }
  .company__trade { font-size: 18px; margin-top: 4px; }
  .company__address { font-size: 18px; margin-top: 1px; }
  .contact-list { list-style: none; margin-top: 10px; font-size: 18px; line-height: 1.3; }
  .contact-list__label {
    color: var(--brand-blue); display: inline-block; width: 74px; text-align: left; margin-left: 6px;
  }
  .company__web { font-size: 18px; margin-top: 6px; }
  .person__email {
    position: absolute; right: 36px; top: 360px;
    font-size: 18px; font-weight: 700; color: var(--ink);
  }
  .person {
    position: absolute; left: 40px; top: 446px; color: var(--ink);
  }
  .person__name {
    font-weight: 900; font-size: 28px; text-transform: uppercase; letter-spacing: .5px;
  }
  .person__divider { margin: 0 12px; font-weight: 400; }
  .person__phone { font-size: 20px; font-weight: 700; margin-top: 12px; }
</style>
</head>
<body>
  <div class="card">
    <div class="card__band"></div>
    <div class="card__band-raised"></div>

    <svg class="card__photo" viewBox="0 0 540 422" role="img" aria-label="Portrait photo of the card holder in a dark suit against a grey studio backdrop">
      <defs>
        <radialGradient id="studio" cx="45%" cy="40%" r="70%">
          <stop offset="0" stop-color="#55595e"/>
          <stop offset="1" stop-color="#2b2d30"/>
        </radialGradient>
      </defs>
      <path d="M0 0 H330 C430 100 505 250 495 422 H0 Z" fill="url(#studio)"/>
      <path d="M330 0 C430 100 505 250 495 422" fill="none" stroke="#2456c4" stroke-width="7"/>
    </svg>

    <div class="company">
      <div class="company__name"><span class="company__mark"></span>K &amp; R Fabrications, Inc.</div>
      <p class="company__trade">Mechanical Contractor</p>
      <p class="company__address">4150 Harlow Road, Brookfield, WI 53005-1120</p>
      <ul class="contact-list">
        <li>555-301-4418<span class="contact-list__label">: Direct</span></li>
        <li>555-301-7720<span class="contact-list__label">: Office</span></li>
        <li>555-301-7791<span class="contact-list__label">: Fax</span></li>
        <li>krfabrications-demo.com<span class="contact-list__label">: Web</span></li>
      </ul>
      <p class="company__web">www.krfabrications-demo.com</p>
    </div>

    <p class="person__email">E-mail : danielmorrow@krfabrications-demo.com</p>

    <div class="person">
      <p class="person__name">Daniel Morrow<span class="person__divider">|</span>Title</p>
      <p class="person__phone">Phone : +123 456 7890</p>
    </div>
  </div>
</body>
</html>
```